Logo for KEX Co. roofing company
KEX, Co.
Professional
Dalmon Fitch
Owner
17 Hollet Lane Harlow, NH 02974
Estimates
kexcoroofing@brightpost.net
kexcoroofing.net
Fully Insured
I want long used as the focus point. Company colors: Primary- Green, secondary- Black and yellow. on the back of the card I want kexcoroofing.net to be centered
brambeek brambeek
Please upload your logo Ai file.. thanks
Fitch42 Fitch42
I already have a logo that was previously made for me, I would like for that logo to be used.

```html
<!DOCTYPE html>
<html lang="en">
<head>
<meta charset="utf-8">
<title>KEX Co. Business Card</title>
<link rel="stylesheet" href="https://fonts.googleapis.com/css2?family=Cinzel:wght@400;600;700&display=swap">
<style>
  :root {
    --green: #3f9a34;
    --green-dark: #2e7d26;
    --green-light: #5cb84a;
    --green-pale: #dcefd6;
    --ink: #3a3a3a;
    --muted: #777;
    --paper: #ffffff;
    --backdrop: #ecebe8;
  }
  * { box-sizing: border-box; margin: 0; padding: 0; }
  html, body { width: 1200px; height: 901px; overflow: hidden; }
  body {
    background: var(--backdrop);
    font-family: "Cinzel", serif;
    position: relative;
  }
  .card {
    position: absolute;
    top: 296px;
    width: 540px;
    height: 309px;
    border-radius: 4px;
    box-shadow: 0 6px 18px rgba(0,0,0,0.18);
    overflow: hidden;
  }
  .card-front { left: 40px; background: var(--paper); }
  .card-back {
    left: 620px;
    background: linear-gradient(135deg, var(--green-light), var(--green-dark));
    color: var(--paper);
  }
  .front-band {
    position: absolute;
    left: 0; top: 0; bottom: 0;
    width: 190px;
    background: linear-gradient(160deg, rgba(255,255,255,0) 20%, var(--green-pale) 100%);
  }
  .front-info {
    position: absolute;
    right: 34px; top: 28px;
    text-align: right;
    color: var(--ink);
  }
  .brand {
    display: flex;
    align-items: center;
    justify-content: flex-end;
    gap: 10px;
    color: var(--green);
    font-weight: 700;
    font-size: 30px;
    letter-spacing: 2px;
    margin-bottom: 22px;
  }
  .brand-mark {
    width: 14px; height: 14px;
    background: var(--green);
  }
  .person-name {
    color: var(--green);
    font-weight: 700;
    font-size: 20px;
    letter-spacing: 1px;
  }
  .person-role {
    font-size: 10px;
    color: var(--muted);
    letter-spacing: 1px;
    margin-bottom: 14px;
  }
  .address, .contacts { font-size: 12px; line-height: 1.45; }
  .address { margin-bottom: 10px; }
  .contacts .label { color: var(--green); font-weight: 600; margin-right: 6px; }
  .back-url {
    position: absolute;
    top: 44px; left: 0; right: 0;
    text-align: center;
    font-size: 15px;
    letter-spacing: 2px;
  }
  .back-brand {
    position: absolute;
    top: 130px; left: 0; right: 0;
    display: flex;
    align-items: center;
    justify-content: center;
    gap: 16px;
    font-size: 54px;
    font-weight: 700;
    letter-spacing: 4px;
  }
  .back-brand .brand-mark { width: 22px; height: 22px; background: var(--paper); }
</style>
</head>
<body>
  <section class="card card-front">
    <div class="front-band"></div>
    <div class="front-info">
      <div class="brand"><span class="brand-mark"></span>KEX Co.</div>
      <div class="person-name">Dalmon Fitch</div>
      <div class="person-role">Owner</div>
      <div class="address">
        <div>17 Hollet Lane</div>
        <div>Harlow, NH 02974</div>
      </div>
      <div class="contacts">
        <div><span class="label">Phone</span>555-301-0142</div>
        <div><span class="label">Cell</span>555-301-0187</div>
        <div><span class="label">Fax</span>555-302-0163</div>
        <div>kexcoroofing@brightpost.net</div>
        <div>www.kexcoroofing.net</div>
      </div>
    </div>
  </section>

  <section class="card card-back">
    <div class="back-url">www.kexcoroofing.net</div>
    <div class="back-brand"><span class="brand-mark"></span>KEX Co.</div>
  </section>
</body>
</html>
```